Maple's Pantry Home Page Design

Hello ArtHivePro -

I am looking for a home page design for an Indian Food Grocery ecommerce site with a store in Boulder, CO. This design request is just for the home page (http://maplespantry.com/), including new design, font, layout and emblem/word mark logo.

What: Maple's Pantry (spices, lentils, rice, frozen foods, etc.)

Desired Color Scheme: Warm, earth tones (red, orange, yellow), that remind the guest of Indian Spices

Tone: This is an Indian-American family owned, small business catering imported Indian foods and spices to a primary market of Indian-Americans and a secondary market of Indian food/spice lovers.

Themes to communicate: Indian, family owned, food

Sample Websites: http://www.brivantfare.com/, http://www.tolvacart.com/, http://www.quenlarmart.com/

Please feel free to reach out with any questions. Thank you.

Target Market(s)

Indian-Americans (1st and 2nd Generation)

Industry/Entity Type

Small Business

Requirements
Must have
• Final Design must be delivered in layered PSD file with all fonts and licenses used.

```html
<!DOCTYPE html>
<html lang="en">
<head>
<meta charset="utf-8">
<title>Maple's Pantry</title>
<link rel="stylesheet" href="https://fonts.googleapis.com/css2?family=Source+Sans+3:wght@400;600&display=swap">
<style>
:root{
  --orange:#f7861c;
  --orange-dark:#e9700c;
  --orange-text:#f26b1d;
  --red:#d8242b;
  --blue:#1a8fd8;
  --ink:#222;
  --line:#d9d9d9;
  --nav-grey:#f1f1f1;
  --footer:#f4f4f4;
}
*{box-sizing:border-box;margin:0;padding:0}
html,body{width:1168px;height:1200px;overflow:hidden;background:#fff}
body{position:relative;font-family:"Source Sans 3",Arial,sans-serif;color:var(--ink);border-top:2px solid #ddd}
.abs{position:absolute}
.brand{left:147px;top:12px;font-size:28px;font-weight:400;color:var(--red);letter-spacing:.3px}
.account{right:150px;top:20px;font-size:12px;color:var(--orange-text);display:flex;gap:10px;align-items:center}
.account a{color:var(--orange-text);text-decoration:underline}
.account .count{font-size:16px}
.account .sep{width:1px;height:16px;background:#ccc}
.nav{left:149px;width:869px;display:flex;font-size:11px}
.nav span{flex:auto;text-align:center;white-space:nowrap;line-height:26px}
.nav-main{top:56px;height:26px;background:linear-gradient(#f99a2e,#f07d12);color:#fff}
.nav-main span+span{border-left:1px solid #fbb36a}
.nav-sub{top:84px;height:28px;background:linear-gradient(#fff,#eaeaea);color:#333}
.nav-sub span{line-height:28px}
.nav-sub span+span{border-left:1px solid #d0d0d0}
.hero{left:149px;top:120px;width:682px;height:312px;background:linear-gradient(110deg,#c7cdd3 0%,#e6e1d8 35%,#bfc9cf 60%,#d7c6a6 100%);box-shadow:0 6px 8px -4px rgba(0,0,0,.4);overflow:hidden}
.hero-caption{position:absolute;left:0;top:87px;width:304px;height:141px;background:rgba(255,255,255,.55);padding:10px 0 0 30px;font-size:23px;line-height:29.5px;color:#111;white-space:nowrap}
.dots{position:absolute;left:302px;top:293px;width:78px;height:26px;background:#fff;border-radius:40px 40px 0 0;display:flex;gap:5px;justify-content:center;padding-top:8px}
.dots i{width:8px;height:8px;border-radius:50%;background:#ccc}
.dots i.on{background:var(--red)}
.perk{left:840px;width:180px;border:1px solid var(--line);background:#fff}
.perk svg{position:absolute;left:14px}
.perk .t{position:absolute;left:59px;font-size:18px;line-height:21px;color:var(--blue)}
.bar{left:149px;top:461px;width:869px;height:27px;background:linear-gradient(#f99a2e,#f07d12);color:#fff;font-size:15px;line-height:27px;padding-left:12px}
.products{left:149px;top:500px;width:869px;height:205px;display:flex}
.product{flex:1;text-align:center;position:relative}
.product+.product{border-left:1px solid #e3e3e3}
.product .img{width:142px;height:128px;margin:2px auto 0;border-radius:4px}
.product h3{font-weight:400;font-size:20px;color:var(--orange-text);margin-top:14px;line-height:22px}
.product .price{font-size:11px;margin-top:3px}
.btn{display:inline-flex;align-items:center;gap:6px;background:var(--orange);color:#fff;border-radius:2px;font-size:13px;height:22px;padding:0 8px;margin-top:7px}
.card{top:746px;width:270px;height:189px;border:1px solid var(--line);background:#fff;overflow:hidden}
.card h4{position:absolute;left:16px;top:14px;font-weight:400;font-size:14px;color:var(--orange-text)}
.card .img{position:absolute;left:16px;top:39px;width:238px;height:104px}
.card p{position:absolute;left:16px;top:150px;width:240px;font-size:11px;line-height:16px}
.more{top:941px;height:21px;background:var(--orange);color:#fff;font-size:11px;line-height:21px;padding:0 6px;display:flex;align-items:center;gap:4px;border-radius:2px}
.more b{width:11px;height:11px;background:#fbc38c;color:var(--orange);font-size:10px;line-height:11px;text-align:center;font-weight:600}
.footer{left:155px;top:997px;width:873px;height:203px;background:linear-gradient(#fff,var(--footer));border:1px solid #e6e6e6;border-bottom:0}
.footer h5{position:absolute;font-weight:400;color:var(--orange-text)}
.field{position:absolute;top:43px;width:204px;height:27px;border:1px solid #ddd;background:#fff;font-size:11px;color:#555;line-height:25px;padding-left:10px;box-shadow:inset 0 1px 2px rgba(0,0,0,.08)}
.subscribe{position:absolute;left:443px;top:47px;height:21px;background:var(--orange);color:#fff;font-size:12px;line-height:21px;padding:0 6px;border-radius:2px}
.social{position:absolute;right:20px;top:44px;display:flex;gap:8px}
.social i{width:21px;height:21px;border-radius:3px;display:block}
.rule{position:absolute;left:20px;width:834px;height:1px;background:#ddd}
.links{position:absolute;left:0;right:0;top:127px;text-align:center;font-size:11px;color:var(--orange-text)}
.links span+span::before{content:"|";margin:0 6px;color:var(--orange-text)}
.copy{position:absolute;left:0;right:0;top:173px;text-align:center;font-size:10px}
</style>
</head>
<body>
<div class="abs brand">Maple's Pantry</div>
<div class="abs account">
  <svg width="15" height="13" viewBox="0 0 15 13"><path d="M0 1h3l2 7h7l2-5H4" fill="none" stroke="#333" stroke-width="1.4"/><circle cx="6" cy="11" r="1.2" fill="#333"/><circle cx="11" cy="11" r="1.2" fill="#333"/></svg>
  <a>Shopping Cart <span class="count">(0)</span> items</a><span class="sep"></span><a>Login</a>
</div>

<nav class="abs nav nav-main">
  <span>ARYUVEDIC</span><span>DRINKS &amp; MIXES</span><span>DRY FRUIT</span><span>NUTS &amp; LEAVES</span><span>DAIRY</span><span>JAGGERY &amp; SUGARS</span><span>EZ-TO-MAKE</span><span>FLOUR &amp; WHEAT</span><span>KITCHENWARE</span><span>SAUCES &amp; PASTES</span>
</nav>
<nav class="abs nav nav-sub">
  <span>POOJA / RELIGIOUS</span><span>LENTIL, DALS &amp; BEANS</span><span>CONCERATES</span><span>SRYUPS &amp; MOLASSES</span><span>NOODLES &amp; SOUPS</span><span>RICE</span><span>COSMETICS/BEAUTY</span><span>MIDDLE EASTERN FOODS</span>
</nav>

<div class="abs hero" role="img" aria-label="Shopper picking products from a grocery store shelf">
  <div class="hero-caption">Lorem Ipsum is simply<br>dummy text of the<br>printing and typesetting<br>industry.</div>
  <div class="dots"><i></i><i></i><i class="on"></i><i></i><i></i></div>
</div>

<div class="abs perk" style="top:133px;height:67px">
  <svg style="top:14px" width="30" height="34" viewBox="0 0 30 34"><path d="M4 4h22M4 12h22M4 4h8a8 8 0 0 1 0 16H6l14 12" fill="none" stroke="var(--blue)" stroke-width="3.5"/></svg>
  <div class="t" style="top:12px">Pay Cash on<br>Delivery</div>
</div>
<div class="abs perk" style="top:222px;height:67px">
  <svg style="top:16px" width="34" height="32" viewBox="0 0 34 32"><path d="M3 15L17 3l14 12" fill="none" stroke="var(--blue)" stroke-width="4"/><rect x="7" y="14" width="20" height="16" fill="#f2b866"/><rect x="14" y="20" width="6" height="10" fill="#fff"/></svg>
  <div class="t" style="top:12px">Free Home<br>Delviery</div>
</div>
<div class="abs perk" style="top:309px;height:111px">
  <svg style="top:14px" width="36" height="40" viewBox="0 0 36 40"><circle cx="20" cy="8" r="7" fill="#3aa5e6"/><path d="M8 32a12 12 0 0 1 24 0z" fill="#3aa5e6"/><circle cx="10" cy="28" r="7" fill="none" stroke="var(--blue)" stroke-width="3"/></svg>
  <div class="t" style="top:10px">Customer<br>Support</div>
  <div class="t" style="top:57px;color:var(--orange-text)">415.XXX.XXX</div>
  <div class="t" style="top:83px;font-size:12px;color:#111">9 AM to 7 PM</div>
</div>

<div class="abs bar">LATEST ARRIVALS</div>

<section class="abs products">
  <div class="product"><div class="img" role="img" aria-label="Herbs in a mortar and pestle" style="background:radial-gradient(#e4ecd9,#fff 70%)"></div><h3>Aryuvedic</h3><div class="price">Rs. 10,200.00</div><span class="btn"><svg width="14" height="12" viewBox="0 0 15 13"><path d="M0 1h3l2 7h7l2-5H4" fill="none" stroke="#fff" stroke-width="1.6"/><circle cx="6" cy="11" r="1.3" fill="#fff"/><circle cx="11" cy="11" r="1.3" fill="#fff"/></svg>Add to Cart</span></div>
  <div class="product"><div class="img" role="img" aria-label="Bowl of white rice" style="background:radial-gradient(#f1f1ee,#fff 70%)"></div><h3>Rice</h3><div class="price">Rs. 10,200.00</div><span class="btn"><svg width="14" height="12" viewBox="0 0 15 13"><path d="M0 1h3l2 7h7l2-5H4" fill="none" stroke="#fff" stroke-width="1.6"/><circle cx="6" cy="11" r="1.3" fill="#fff"/><circle cx="11" cy="11" r="1.3" fill="#fff"/></svg>Add to Cart</span></div>
  <div class="product"><div class="img" role="img" aria-label="Round tray of assorted spices" style="background:radial-gradient(#8a5a3a,#c9863a 45%,#fff 72%)"></div><h3>Spices</h3><div class="price">Rs. 10,200.00</div><span class="btn"><svg width="14" height="12" viewBox="0 0 15 13"><path d="M0 1h3l2 7h7l2-5H4" fill="none" stroke="#fff" stroke-width="1.6"/><circle cx="6" cy="11" r="1.3" fill="#fff"/><circle cx="11" cy="11" r="1.3" fill="#fff"/></svg>Add to Cart</span></div>
  <div class="product"><div class="img" role="img" aria-label="Glasses of colourful fruit drinks" style="background:linear-gradient(90deg,#f2c27a,#e9876a,#f06a8a)"></div><h3>Drinks &amp; Mixes</h3><div class="price">Rs. 10,200.00</div><span class="btn"><svg width="14" height="12" viewBox="0 0 15 13"><path d="M0 1h3l2 7h7l2-5H4" fill="none" stroke="#fff" stroke-width="1.6"/><circle cx="6" cy="11" r="1.3" fill="#fff"/><circle cx="11" cy="11" r="1.3" fill="#fff"/></svg>Add to Cart</span></div>
  <div class="product"><div class="img" role="img" aria-label="Sacks and bowls of flour and grains" style="background:radial-gradient(#e8dcc6,#fff 72%)"></div><h3>Flour &amp; Wheat</h3><div class="price">Rs. 10,200.00</div><span class="btn"><svg width="14" height="12" viewBox="0 0 15 13"><path d="M0 1h3l2 7h7l2-5H4" fill="none" stroke="#fff" stroke-width="1.6"/><circle cx="6" cy="11" r="1.3" fill="#fff"/><circle cx="11" cy="11" r="1.3" fill="#fff"/></svg>Add to Cart</span></div>
</section>

<div class="abs card" style="left:155px">
  <h4>ABOUT US</h4>
  <div class="img" role="img" aria-label="Grocery store aisle with stocked shelves" style="background:linear-gradient(90deg,#8fa0b8,#d9b77a,#b9c7d6)"></div>
  <p>Lorem Ipsum is simply dummy text of the rinting and typesetting industry.</p>
</div>
<div class="abs more" style="left:338px">READ MORE <b>+</b></div>

<div class="abs card" style="left:457px">
  <h4>SPECIALS &amp; CLEARANCE</h4>
  <div class="img" role="img" aria-label="Assortment of fresh vegetables, fruit and groceries" style="background:radial-gradient(ellipse at 50% 70%,#d9732f,#8bb04a 45%,#fff 75%)"></div>
  <p>Lorem Ipsum is simply dummy text of the rinting and typesetting industry.</p>
</div>
<div class="abs more" style="left:639px">READ MORE <b>+</b></div>

<div class="abs card" style="left:756px">
  <div class="abs" style="left:25px;top:22px;font-size:20px;line-height:30px;color:var(--orange-text)">100% Customer<br>Satisfaction<br>Guaranteed</div>
  <p style="left:25px;top:117px;width:125px">Lorem Ipsum is simply dummy text of the rinting...</p>
  <svg class="abs" style="left:152px;top:38px" width="106" height="106" viewBox="0 0 106 106"><circle cx="53" cy="53" r="52" fill="#8c8c8c"/><circle cx="53" cy="53" r="37" fill="#2a2a2a"/></svg>
</div>
<div class="abs more" style="left:939px">READ MORE <b>+</b></div>

<footer class="abs footer">
  <h5 style="left:20px;top:22px;font-size:15px">NEWSLETTER SIGNUP</h5>
  <h5 style="right:20px;top:25px;font-size:12px">FOLLOW US ON</h5>
  <div class="field" style="left:20px">Enter the E mail id</div>
  <div class="field" style="left:232px">Enter the Name</div>
  <div class="subscribe">SUBSCRIBE</div>
  <div class="social"><i style="background:#3b5ea8"></i><i style="background:#41a9e0"></i><i style="background:#f08a24"></i><i style="background:#1a77b5"></i></div>
  <div class="rule" style="top:114px"></div>
  <div class="links"><span>Terms &amp; Conditions</span><span>Privacy Policy</span><span>Contact Us</span></div>
  <div class="rule" style="top:163px"></div>
  <div class="copy">© 2012 Maple's Pantry All right reserved.</div>
</footer>
</body>
</html>
```